I need the following on my business card:
- Name: Dana Whitcomb
- License # 0M93216
- Title: Producer
- Phone: (555) 017-3904
- Email: Dana@CorbelInsuranceServices.com

- Company: Corbel Insurance Services
- Address: 27408 Larkmoor Ave Suite 610, Alder Heights, CA 90217
- Website: www.CorbelInsuranceServices.com

Also add our slogan on the card: "Steady Cover, Honest Advice"

```html
<!DOCTYPE html>
<html lang="en">
<head>
<meta charset="utf-8">
<title>Corbel Insurance Services – Business Card</title>
<link rel="stylesheet" href="https://fonts.googleapis.com/css2?family=Montserrat:wght@400;500;700;800&display=swap">
<style>
  :root {
    --navy: #2b3585;
    --green: #1f9a4a;
    --ink: #3a3a3a;
    --muted: #6b6b6b;
    --paper: #ffffff;
    --backdrop: #e9eaee;
  }
  * { box-sizing: border-box; margin: 0; padding: 0; }
  html, body { width: 1200px; height: 900px; overflow: hidden; }
  body {
    background: var(--backdrop);
    font-family: "Montserrat", sans-serif;
    display: flex;
    flex-direction: column;
    align-items: center;
    justify-content: center;
    gap: 52px;
  }
  .card {
    position: relative;
    width: 620px;
    height: 354px;
    border-radius: 22px;
    overflow: hidden;
    box-shadow: 0 8px 24px rgba(0,0,0,0.12);
  }
  .card-front { background: var(--paper); }
  .card-back {
    background: var(--navy);
    display: flex;
    align-items: center;
    justify-content: center;
  }

  /* wordmark */
  .wordmark { display: flex; flex-direction: column; line-height: 1; }
  .wordmark-name {
    font-weight: 800;
    text-transform: uppercase;
    letter-spacing: 1px;
  }
  .wordmark-sub {
    font-weight: 800;
    text-transform: uppercase;
  }
  .card-front .wordmark {
    position: absolute; right: 36px; top: 44px;
    color: var(--navy); align-items: flex-end;
  }
  .card-front .wordmark-name { font-size: 50px; }
  .card-front .wordmark-sub { font-size: 15px; margin-top: 8px; letter-spacing: 5.2px; }
  .card-back .wordmark { color: var(--paper); align-items: center; }
  .card-back .wordmark-name { font-size: 82px; }
  .card-back .wordmark-sub { font-size: 22px; margin-top: 14px; letter-spacing: 9px; }

  /* person */
  .person { position: absolute; left: 34px; top: 46px; }
  .person-name {
    color: var(--green); font-weight: 800; font-size: 25px;
    text-transform: uppercase; letter-spacing: 0.5px; white-space: nowrap;
  }
  .person-title { color: var(--muted); font-size: 13px; margin-top: 4px; }

  .rule {
    position: absolute; left: 34px; top: 142px;
    width: 250px; height: 2px; background: var(--green);
  }
  .band {
    position: absolute; top: 129px; height: 30px;
    display: flex; align-items: center;
    color: var(--paper); font-size: 12px; font-weight: 500;
    white-space: nowrap;
  }
  .band-slogan {
    left: 270px; width: 215px; background: var(--navy);
    padding-left: 20px;
    clip-path: polygon(0 0, 100% 0, 100% 100%, 14px 100%);
  }
  .band-license {
    left: 485px; right: 0; background: var(--green);
    padding-left: 10px;
  }

  .contacts {
    position: absolute; left: 34px; top: 190px;
    list-style: none; color: var(--ink); font-size: 12.5px;
  }
  .contacts li { display: flex; align-items: center; gap: 8px; margin-bottom: 9px; }
  .contacts svg { width: 12px; height: 12px; fill: var(--green); flex: none; }

  .address {
    position: absolute; right: 34px; bottom: 34px;
    text-align: right; color: var(--ink); font-size: 13px; line-height: 1.55;
    font-style: normal;
  }
  .address-company { font-weight: 700; }
</style>
</head>
<body>

<section class="card card-front">
  <div class="wordmark">
    <span class="wordmark-name">Corbel</span>
    <span class="wordmark-sub">Insurance Services</span>
  </div>

  <div class="person">
    <h1 class="person-name">Dana Whitcomb</h1>
    <p class="person-title">Producer</p>
  </div>

  <div class="rule"></div>
  <div class="band band-slogan">Steady Cover, Honest Advice</div>
  <div class="band band-license">License # 0M93216</div>

  <ul class="contacts">
    <li>
      <svg viewBox="0 0 24 24" aria-hidden="true"><path d="M6.6 10.8a15 15 0 0 0 6.6 6.6l2.2-2.2c.3-.3.7-.4 1-.2 1.1.4 2.3.6 3.6.6.6 0 1 .4 1 1V20c0 .6-.4 1-1 1C10.6 21 3 13.4 3 4c0-.6.4-1 1-1h3.5c.6 0 1 .4 1 1 0 1.3.2 2.5.6 3.6.1.3 0 .7-.2 1z"/></svg>
      (555) 017-3904
    </li>
    <li>
      <svg viewBox="0 0 24 24" aria-hidden="true"><path d="M2 5h20v14H2zM4 7v.5l8 5 8-5V7l-8 5z"/></svg>
      Dana@CorbelInsuranceServices.com
    </li>
    <li>
      <svg viewBox="0 0 24 24" aria-hidden="true"><circle cx="12" cy="12" r="10"/></svg>
      www.CorbelInsuranceServices.com
    </li>
  </ul>

  <address class="address">
    <span class="address-company">Corbel Insurance Services</span><br>
    27408 Larkmoor Ave Suite 610,<br>
    Alder Heights, CA 90217
  </address>
</section>

<section class="card card-back">
  <div class="wordmark">
    <span class="wordmark-name">Corbel</span>
    <span class="wordmark-sub">Insurance Services</span>
  </div>
</section>

</body>
</html>
```